Flyer-Design für private Musikakademie
Zielgruppe
Unsere Firma ist eine private Musikakademie für klassische Musik. Die Zielgruppe sind internationale Studenten und Publikum
Aufgabenstellung
Klassisch, elegant.
Wir benötigen einen Flyer im in zwei gefalteten A4 format (4 Seiten A5) für ein Festival in 2 Wochen.
Ausserdem benötigen wir einen stehenden Banner (ca. 2 m hoch) mit dem Hauptlogo und der Bezeichnung des Festivals.
Bitte kontaktieren Sie mich, falls Sie weiteres Bidmaterial, bzw. weitere Angaben benötigen. Das ist mein erstes aufgegebene Projekt hier.
Die Texteingabe ist in Deutsch/English. Meine Vorstellung wäre Deutsch etwas größer, English etwas versetzt darunter etwas kleiner, vielleicht kursiv, damit man es optisch gut auseinander halten kann

```html
<!DOCTYPE html>
<html lang="de">
<head>
<meta charset="utf-8">
<title>Festival Ablauf – Festival Schedule</title>
<link rel="stylesheet" href="https://fonts.googleapis.com/css2?family=Oswald:wght@400;500&family=Tinos:ital@0;1&family=Roboto+Condensed:ital,wght@1,400&display=swap">
<style>
  :root{
    --teal:#2aa9b5;
    --teal-top:#2bb1bc;
    --teal-bottom:#0f4a50;
    --ink:#1f2a2e;
    --heading:#1d3b40;
    --card:#ffffff;
    --photo-light:#d9d9d9;
    --photo-dark:#6f6f6f;
  }
  *{margin:0;padding:0;box-sizing:border-box}
  html,body{width:1200px;height:849px;overflow:hidden;background:#fff}
  .spread{position:relative;width:1200px;height:849px}

  /* faculty page */
  .faculty{position:absolute;left:0;top:0;width:597px;height:849px;
    background:linear-gradient(180deg,var(--teal-top) 0%,#1f8791 45%,var(--teal-bottom) 100%)}
  .member{position:absolute;width:160px;height:185px}
  .portrait{position:absolute;left:2px;top:0;width:156px;height:156px;border-radius:50%;
    border:4px solid #fff;background:radial-gradient(circle at 50% 40%,var(--photo-light),var(--photo-dark));
    box-shadow:0 2px 6px rgba(0,0,0,.25)}
  .card{position:absolute;left:0;top:130px;width:160px;height:55px;background:var(--card);
    border-radius:10px;box-shadow:0 3px 8px rgba(0,0,0,.3);text-align:center;padding-top:5px}
  .card .name{font-family:"Oswald",sans-serif;font-weight:500;font-size:16px;line-height:18px;color:var(--teal);white-space:nowrap}
  .card .instrument{font-family:"Tinos",serif;font-size:11px;line-height:14px;color:var(--ink)}
  .card .school{font-family:"Roboto Condensed",sans-serif;font-style:italic;font-size:7px;line-height:11px;color:var(--ink);white-space:nowrap}

  /* schedule page */
  .schedule{position:absolute;left:597px;top:0;width:603px;height:849px;background:#fff}
  .schedule-title{position:absolute;left:29px;top:33px;font-family:"Oswald",sans-serif;font-weight:400;font-size:19px;line-height:24px;color:var(--teal)}
  .schedule-title span{font-size:13px;color:var(--heading)}
  .day{position:absolute;left:29px;width:570px}
  .day h2{font-family:"Oswald",sans-serif;font-weight:500;font-size:15px;line-height:19px;height:19px;color:var(--heading)}
  .row{display:flex;height:15.5px;line-height:15.5px;white-space:nowrap;overflow:visible}
  .row.has-sub{height:26px}
  .time{width:84px;flex:none;font-family:"Oswald",sans-serif;font-size:10.5px;color:var(--teal)}
  .item{flex:1;font-family:"Tinos",serif;font-size:11px;color:var(--ink)}
  .item small{font-size:7.5px}
  .item .sub{display:block;font-size:7.2px;line-height:9px}
  .note{position:absolute;left:29px;top:775px;width:548px;font-family:"Tinos",serif;font-size:10px;line-height:12px;color:var(--ink)}
  .note small{font-size:7.2px}
</style>
</head>
<body>
<div class="spread">

  <section class="faculty">
    <div class="member" style="left:27px;top:27px">
      <div class="portrait" role="img" aria-label="Portrait photo of the piano professor"></div>
      <div class="card"><div class="name">PROF. ANTON MARVIK</div><div class="instrument">Klavier / Piano</div><div class="school">President - Music Academy Neue Klänge Nordstadt</div></div>
    </div>
    <div class="member" style="left:219px;top:27px">
      <div class="portrait" role="img" aria-label="Portrait photo of the piano professor at a grand piano"></div>
      <div class="card"><div class="name">PROF. IVO SCHELL</div><div class="instrument">Klavier / Piano</div><div class="school">Musikhochschule Nordstadt</div></div>
    </div>
    <div class="member" style="left:410px;top:27px">
      <div class="portrait" role="img" aria-label="Portrait photo of the piano professor"></div>
      <div class="card"><div class="name">PROF. EVA KORLAN</div><div class="instrument">Klavier / Piano</div><div class="school">Musikhochschule Nordstadt</div></div>
    </div>

    <div class="member" style="left:133px;top:226px">
      <div class="portrait" role="img" aria-label="Portrait photo of the violin professor with her violin"></div>
      <div class="card"><div class="name">PROF. AGNES ULNER</div><div class="instrument">Geige / Violin</div><div class="school">Musikhochschule Elbtal</div></div>
    </div>
    <div class="member" style="left:340px;top:226px">
      <div class="portrait" role="img" aria-label="Portrait photo of the cello professor with his cello"></div>
      <div class="card"><div class="name">PROF. MAREK SOLINSKI</div><div class="instrument">Cello</div><div class="school">Music Academy Vellano</div></div>
    </div>

    <div class="member" style="left:27px;top:423px">
      <div class="portrait" role="img" aria-label="Portrait photo of the cello and orchestra teacher"></div>
      <div class="card"><div class="name">LEO GARAN</div><div class="instrument">Cello/Orchestra Class</div><div class="school">Music Academy Neue Klänge Nordstadt</div></div>
    </div>
    <div class="member" style="left:219px;top:423px">
      <div class="portrait" role="img" aria-label="Portrait photo of the piano teacher"></div>
      <div class="card"><div class="name">MIRA BALANOVA</div><div class="instrument">Klavier / Piano</div><div class="school">Music Academy Neue Klänge Nordstadt</div></div>
    </div>
    <div class="member" style="left:410px;top:423px">
      <div class="portrait" role="img" aria-label="Portrait photo of the composition teacher"></div>
      <div class="card"><div class="name">DAVID MERHOLT</div><div class="instrument">Komposition / Composition</div><div class="school">Music Academy Neue Klänge Nordstadt</div></div>
    </div>

    <div class="member" style="left:133px;top:636px">
      <div class="portrait" role="img" aria-label="Portrait photo of the voice teacher"></div>
      <div class="card"><div class="name">NADIA SORELSKAYA</div><div class="instrument">Gesang / Voice</div><div class="school">Musikhochschule Nordstadt</div></div>
    </div>
    <div class="member" style="left:340px;top:636px">
      <div class="portrait" role="img" aria-label="Portrait photo of the piano teacher"></div>
      <div class="card"><div class="name">RENATA CHERVENKO</div><div class="instrument">Klavier / Piano</div><div class="school">Music Academy Neue Klänge Nordstadt</div></div>
    </div>
  </section>

  <section class="schedule">
    <h1 class="schedule-title">FESTIVAL ABLAUF <span>/ FESTIVAL SCHEDULE</span></h1>

    <div class="day" style="top:74px">
      <h2>AUGUST 6, 2018</h2>
      <div class="row"><div class="time">14:00</div><div class="item">Registrierung der Teilnehmer <small>/ Participants registration</small></div></div>
      <div class="row"><div class="time">17:00</div><div class="item">Pressekonferenz <small>/ Press conference</small></div></div>
      <div class="row has-sub"><div class="time">18:00</div><div class="item">Eröffnungskonzert des 1. Internationalen Musikfestivals „Nordstadt-Klassik“<span class="sub">/ Opening concert of the 1-st „Nordstadt-Klassik“ international festival</span></div></div>
    </div>

    <div class="day" style="top:174px">
      <h2>AUGUST 7, 2018</h2>
      <div class="row"><div class="time">10:00 – 13:00</div><div class="item">Meisterkurse für Klavier, Gesang und Komposition <small>/ Master Classes for piano, voice and composition</small></div></div>
      <div class="row"><div class="time"></div><div class="item">Mittagspause <small>/ Lunch Break</small></div></div>
      <div class="row"><div class="time">14:30 – 17:30</div><div class="item">Meisterkurse für Klavier, Gesang und Schlagzeug <small>/ Master Classes for piano, voice and percussion</small></div></div>
      <div class="row"><div class="time">14:30 – 17:30</div><div class="item">Orchesterprobe <small>/ Orchestra rehearsal</small></div></div>
      <div class="row"><div class="time">18:00</div><div class="item">Konzert der Professoren und Dozenten <small>/ Faculty concert</small></div></div>
    </div>

    <div class="day" style="top:286px">
      <h2>AUGUST 8, 2018</h2>
      <div class="row"><div class="time">14:30 – 17:30</div><div class="item">Meisterkurse für Klavier, Gesang und Schlagzeug <small>/ Master Classes for piano, voice and percussion</small></div></div>
      <div class="row"><div class="time">14:30 – 17:30</div><div class="item">Orchesterprobe <small>/ Orchestra rehearsal</small></div></div>
      <div class="row has-sub"><div class="time">18:30</div><div class="item">Konzert der Festivalteilnehmer und Gästen in der KHNS<span class="sub">/ Concert of the festival participants and guests at the KHNS</span></div></div>
      <div class="row"><div class="time">20:00</div><div class="item">Begrüßung und Empfang <small>/ Greeting and refreshments</small></div></div>
    </div>

    <div class="day" style="top:393px">
      <h2>AUGUST 9, 2018</h2>
      <div class="row"><div class="time">10:00 – 13:00</div><div class="item">Meisterkurse Klavier, Gesang <small>/ Master Classes for piano and voice</small></div></div>
      <div class="row"><div class="time">10:00 – 13:00</div><div class="item">Orchesterprobe <small>/ Orchestra rehearsal</small></div></div>
      <div class="row"><div class="time">10:00 – 13:00</div><div class="item">Internationaler Wettbewerb <small>/ International competition</small></div></div>
      <div class="row"><div class="time"></div><div class="item">Mittagspause <small>/ Lunch Break</small></div></div>
      <div class="row"><div class="time">14:30 – 18:30</div><div class="item">Meisterkurse für alle Instrumente <small>/ Master Classes for all instruments</small></div></div>
      <div class="row"><div class="time">14:30 – 18:30</div><div class="item">Internationaler Wettbewerb <small>/ International competition</small></div></div>
    </div>

    <div class="day" style="top:520px">
      <h2>AUGUST 10, 2018</h2>
      <div class="row"><div class="time">10:00 – 13:00</div><div class="item">Internationaler Wettbewerb <small>/ International competition</small></div></div>
      <div class="row"><div class="time"></div><div class="item">Mittagspause <small>/ Lunch Break</small></div></div>
      <div class="row"><div class="time">14:30 – 17:00</div><div class="item">Internationaler Wettbewerb <small>/ International competition</small></div></div>
      <div class="row"><div class="time">17:30 – 19:00</div><div class="item">Internationaler Wettbewerb <small>/ International competition</small></div></div>
      <div class="row"><div class="time">19:30</div><div class="item">Ankündigung der Wettbewerbspreisträger <small>/ Competition Prize Winner Announcement</small></div></div>
      <div class="row has-sub"><div class="time">20:00</div><div class="item">Konzert der Meisterkursteilnehmer und Zertifikat Verleihung für Meisterkurs Teilnehmer<span class="sub">/ Master Course participants concert and certificate ceremony</span></div></div>
    </div>

    <div class="day" style="top:657px">
      <h2>AUGUST 11, 2018</h2>
      <div class="row"><div class="time">10:00 – 13:00</div><div class="item">Generalprobe Orchester <small>/ General Rehearsal Orchestra</small></div></div>
      <div class="row"><div class="time"></div><div class="item">Mittagspause <small>/ Lunch Break</small></div></div>
      <div class="row"><div class="time">14:30 – 18:30</div><div class="item">Meisterkurse für alle Instrumente <small>/ Master Classes for all instruments</small></div></div>
      <div class="row"><div class="time">19:30</div><div class="item">Wettbewerb Preisverleihung <small>/ Competition Awards Ceremony</small></div></div>
      <div class="row has-sub"><div class="time">20:00</div><div class="item">Abschlusskonzert. Es spielen die Dozenten, Preisträger und Festivalteilnehmer<span class="sub">/ Final concert with the faculty members, award winners and festival participants</span></div></div>
    </div>

    <p class="note">* Änderungen Vorbehalten. Genauere angaben zu den Veranstaltungsorten und einem Ablaufplan entnehmen Sie bitte aus den Aushängen oder sprechen Sie uns an. / <small>Subject to change without notice. Please check possible schedule changes on the black board or contact us for further questions.</small></p>
  </section>

</div>
</body>
</html>
```